Revise our price listr for 2023

Please see attached price list with new prices to revise.
Please include new logo
Please add the text: Please note that prices are subject to change without prior notice.
Please remove prices from equipment with operator
Please add Under Commercial stone:
Fill Dirt $16.
Please add under Decorative Stone:
3/4" Barn Red Stone $127.
3/4" Yellow Ocean Gravel $140.
3/4" Delaware River Gravel $110.
1" Nutmeg Pebble $97.
Price list sending via email and customer in our lobby
Landscape and construction supply

```html
<!DOCTYPE html>
<html lang="en">
<head>
<meta charset="utf-8">
<title>Ridgeway Supply — 2023 Material Price List</title>
<link rel="stylesheet" href="https://fonts.googleapis.com/css2?family=Alfa+Slab+One&family=Archivo+Black&family=Oswald:wght@700&family=Source+Sans+3:wght@400;600;700&display=swap">
<style>
  :root{
    --maroon:#7a1f23;
    --green:#17924a;
    --white:#ffffff;
    --ink:#1c1c1c;
    --rule:#5aa97a;
    --stone-a:#c8a27a;
    --stone-b:#a88360;
    --stone-c:#d9bf9c;
  }
  *{box-sizing:border-box;margin:0;padding:0}
  html,body{width:1200px;height:927px;overflow:hidden;background:#fff}
  body{font-family:'Source Sans 3',sans-serif;color:var(--ink)}
  .sheet{position:relative;width:1200px;height:927px;overflow:hidden}
  .abs{position:absolute}

  .backdrop{position:absolute;inset:0;
    background:radial-gradient(circle at 30% 70%,var(--stone-c),transparent 45%),
               radial-gradient(circle at 80% 30%,var(--stone-c),transparent 40%),
               linear-gradient(135deg,var(--stone-a),var(--stone-b) 50%,var(--stone-a));}
  .hero-photos{position:absolute;left:0;top:0;width:798px;height:248px;
    background:linear-gradient(90deg,#eeeeee 0%,#e4e1dc 28%,#a8835d 42%,#8c6c4d 52%,#6f7454 66%,#566a3f 82%,#8d5a86 100%);}

  .panel{position:absolute;background:var(--white)}
  .panel-left{left:16px;top:217px;width:369px;height:687px}
  .panel-mid{left:415px;top:236px;width:371px;height:668px}
  .panel-right{left:813px;top:26px;width:371px;height:878px}

  .brand{position:absolute;left:104px;top:44px;display:flex;align-items:center;gap:8px;
    font-family:'Oswald',sans-serif;font-weight:700;color:var(--maroon);line-height:1}
  .brand-dot{width:30px;height:30px;border-radius:50%;background:var(--green)}
  .brand-name{font-size:34px;letter-spacing:.5px}
  .brand-name small{display:block;font-size:14px;letter-spacing:6px;margin-top:2px}
  .year{position:absolute;left:138px;top:124px;font-family:'Archivo Black',sans-serif;font-size:50px;color:var(--maroon);line-height:1}
  .title{position:absolute;left:63px;top:170px;font-family:'Oswald',sans-serif;font-weight:700;font-size:33px;color:var(--maroon);line-height:1;transform:scaleY(1.05)}

  .notice{position:absolute;left:16px;top:217px;width:369px;height:36px;background:var(--green);color:#fff;
    font-weight:700;font-size:12.5px;text-align:center;line-height:14px;padding-top:4px}

  .frame{position:absolute;border:3px solid var(--maroon)}
  .tab{position:absolute;background:var(--maroon);color:#fff;font-family:'Alfa Slab One',serif;
    display:flex;align-items:center;justify-content:center;text-align:center;
    writing-mode:vertical-rl;transform:rotate(180deg);font-size:17px;line-height:17px;letter-spacing:.5px}
  .head-tab{position:absolute;background:var(--maroon);color:#fff;font-family:'Alfa Slab One',serif;
    font-size:18px;letter-spacing:1px;display:flex;align-items:center;justify-content:center}
  .link-box{position:absolute;left:596px;top:357px;width:41px;height:16px;border:1px solid var(--maroon);border-top:none;background:#fff}

  .list{position:absolute}
  .row{display:flex;align-items:center;height:24.2px;font-size:15px}
  .item{display:flex;align-items:baseline;white-space:nowrap;overflow:hidden}
  .item::after{content:"";flex:1;border-bottom:1.5px dotted #333;margin-left:3px;transform:translateY(-3px)}
  .price{margin-left:auto;width:52px;height:21px;background:var(--maroon);color:#fff;font-size:15px;
    display:flex;align-items:center;justify-content:center;box-shadow:0 2px 0 #fff,0 3px 0 var(--maroon)}
  .multi{font-size:15px;line-height:13.8px}
  .quote{position:absolute;left:712px;top:830px;width:52px;height:44px;background:var(--maroon);color:#fff;
    font-size:14px;line-height:16px;text-align:center;padding-top:5px}

  .equip-head{position:absolute;left:897px;top:41px;width:212px}
  .equip-head .top{background:var(--maroon);color:#fff;font-family:'Alfa Slab One',serif;font-size:14px;
    letter-spacing:.8px;text-align:center;line-height:17px;height:45px;padding-top:5px}
  .equip-head .bottom{background:var(--green);color:#fff;font-weight:700;font-size:14.5px;text-align:center;height:27px;line-height:27px}
  .rules{position:absolute;left:852px;width:294px}
  .rules .r{position:relative;height:19.8px;border-bottom:1px solid var(--rule);font-size:14.5px;line-height:20px;padding-left:5px;display:flex;white-space:nowrap}
  .rules .r:first-child{border-top:1px solid var(--rule)}
  .rules .r span:nth-child(2){position:absolute;left:168px}
  .bar{position:absolute;left:852px;width:294px;height:23px;background:var(--maroon);color:#fff;font-weight:700;
    font-size:15px;line-height:23px;padding-left:6px}

  .know{position:absolute;left:878px;top:736px;width:241px;height:42px;background:var(--maroon);border-radius:21px;
    color:#fff;font-family:'Alfa Slab One',serif;font-size:17px;letter-spacing:1px;display:flex;align-items:center;padding-left:64px}
  .know svg{position:absolute;left:18px;top:6px}
  .know-text{position:absolute;left:813px;top:790px;width:371px;text-align:center;font-weight:600;font-size:16px;line-height:18px}
  .know-text .accent{color:var(--green)}
  .footer{position:absolute;left:813px;top:868px;width:371px;height:36px;background:var(--green);color:#fff;
    font-weight:700;font-size:13.5px;text-align:center;line-height:36px}
</style>
</head>
<body>
<main class="sheet">
  <div class="backdrop" role="img" aria-label="Close-up of natural tan stone texture"></div>
  <div class="hero-photos" role="img" aria-label="Photos of salt piles, round river stones and a cobblestone garden stairway with purple flowers"></div>

  <div class="panel panel-left"></div>
  <div class="panel panel-mid"></div>
  <div class="panel panel-right"></div>

  <div class="brand"><span class="brand-dot"></span><span class="brand-name">RIDGEWAY<small>SUPPLY</small></span></div>
  <div class="year">2023</div>
  <h1 class="title">MATERIAL PRICE LIST</h1>
  <p class="notice">PLEASE NOTE THAT PRICES ARE SUBJECT TO CHANGE<br>WITHOUT PRIOR NOTICE.</p>

  <div class="frame" style="left:52px;top:268px;width:322px;height:138px"></div>
  <div class="tab" style="left:30px;top:301px;width:45px;height:73px">SOIL</div>
  <div class="list" style="left:85px;top:275px;width:284px">
    <div class="row"><span class="item" style="width:212px">Sandy Loam</span><span class="price">$30</span></div>
    <div class="row"><span class="item" style="width:212px">Topsoil-Screened</span><span class="price">$42</span></div>
    <div class="row"><span class="item" style="width:212px">Garden Soil</span><span class="price">$52</span></div>
    <div class="row"><span class="item" style="width:212px">Mushroom Dirt</span><span class="price">$55</span></div>
    <div class="row"><span class="item" style="width:212px">Compost (Leaf &amp; Grass)</span><span class="price">$55</span></div>
  </div>

  <div class="frame" style="left:52px;top:421px;width:322px;height:160px"></div>
  <div class="tab" style="left:32px;top:440px;width:44px;height:110px">MULCH</div>
  <div class="list" style="left:86px;top:428px;width:284px">
    <div class="row"><span class="item" style="width:212px">Mulch-Dyed Black</span><span class="price">$42</span></div>
    <div class="row"><span class="item" style="width:212px">Mulch-Dyed Red</span><span class="price">$42</span></div>
    <div class="row"><span class="item" style="width:212px">Mulch-Dyed Brown</span><span class="price">$42</span></div>
    <div class="row"><span class="item" style="width:212px">Mulch-Natural Light Brown</span><span class="price">$38</span></div>
    <div class="row"><span class="item" style="width:212px">Mulch-Dark Triple Ground</span><span class="price">$44</span></div>
    <div class="row"><span class="item" style="width:212px">Mulch Cedar</span><span class="price">$55</span></div>
  </div>

  <div class="frame" style="left:52px;top:596px;width:322px;height:286px"></div>
  <div class="tab" style="left:32px;top:662px;width:44px;height:145px">DECORATIVE STONE</div>
  <div class="list" style="left:86px;top:602px;width:284px">
    <div class="row"><span class="item" style="width:220px">White Limestone #1 [1/4”-1/2”]</span><span class="price">$95</span></div>
    <div class="row"><span class="item" style="width:220px">White Limestone #2 [1/2”-3/4”]</span><span class="price">$97.50</span></div>
    <div class="row"><span class="item" style="width:220px">River Rock #2 [3/4”] Round</span><span class="price">$50</span></div>
    <div class="row"><span class="item" style="width:220px">River Rock-Medium [2/3”]</span><span class="price">$95</span></div>
    <div class="row"><span class="item" style="width:220px">River Rounds [4-6”]</span><span class="price">$90</span></div>
    <div class="row"><span class="item" style="width:220px">Pea Gravel</span><span class="price">$50</span></div>
    <div class="row"><span class="item" style="width:220px">Berkshire Blend</span><span class="price">$50</span></div>
    <div class="row"><span class="item" style="width:220px">3/4" Barn Red Stone</span><span class="price">$127</span></div>
    <div class="row"><span class="item" style="width:220px">3/4" Yellow Ocean Gravel</span><span class="price">$140</span></div>
    <div class="row"><span class="item" style="width:220px">3/4" Delaware River Gravel</span><span class="price">$110</span></div>
    <div class="row"><span class="item" style="width:220px">1" Nutmeg Pebble</span><span class="price">$97</span></div>
  </div>

  <div class="frame" style="left:448px;top:266px;width:320px;height:91px"></div>
  <div class="head-tab" style="left:540px;top:252px;width:133px;height:42px">SAND</div>
  <div class="list" style="left:480px;top:297px;width:284px">
    <div class="row"><span class="item" style="width:208px">Masonary/Pool Sand</span><span class="price">$45</span></div>
    <div class="row"><span class="item" style="width:208px">Bedding Sand</span><span class="price">$37</span></div>
  </div>
  <div class="link-box"></div>

  <div class="frame" style="left:446px;top:373px;width:322px;height:258px"></div>
  <div class="tab" style="left:426px;top:415px;width:44px;height:165px">COMMERCIAL STONE</div>
  <div class="list" style="left:478px;top:378px;width:286px">
    <div class="row"><span class="item" style="width:210px">Item #4</span><span class="price">$42</span></div>
    <div class="row"><span class="item" style="width:210px">#1 Stone (1/2”)</span><span class="price">$45</span></div>
    <div class="row"><span class="item" style="width:210px">#2 Stone (3/4” 1”)</span><span class="price">$45</span></div>
    <div class="row"><span class="item" style="width:210px">#3 (1.5* 2*)</span><span class="price">$45</span></div>
    <div class="row"><span class="item" style="width:210px">Stone Chip (fine)</span><span class="price">$40</span></div>
    <div class="row"><span class="item" style="width:210px">Stone Dust (xtra fine)</span><span class="price">$47</span></div>
    <div class="row"><span class="item" style="width:210px">Shale When Available</span><span class="price">Call</span></div>
    <div class="row"><span class="item" style="width:210px">Bank Run Fill (Dirt &amp; Cobble)</span><span class="price">$18</span></div>
    <div class="row"><span class="item" style="width:210px">Crusher Run</span><span class="price">$42</span></div>
    <div class="row"><span class="item" style="width:210px">Fill Dirt</span><span class="price">$16</span></div>
  </div>

  <div class="frame" style="left:444px;top:669px;width:321px;height:56px"></div>
  <div class="head-tab" style="left:540px;top:651px;width:133px;height:41px">SEASONAL</div>
  <div class="list" style="left:477px;top:693px;width:284px">
    <div class="row"><span class="item" style="width:210px">Treated Salt Green</span><span class="price">$165</span></div>
  </div>

  <div class="frame" style="left:444px;top:743px;width:321px;height:139px"></div>
  <div class="tab" style="left:430px;top:756px;width:41px;height:113px;font-size:15px;line-height:16px">DELIVERY CHARGES</div>
  <div class="list" style="left:477px;top:752px;width:287px">
    <div class="row"><span class="item" style="width:210px">Local (Small Truck)</span><span class="price">$165</span></div>
    <div class="row"><span class="item" style="width:210px">Local (Medium Truck)</span><span class="price">$75</span></div>
    <div class="row"><span class="item" style="width:210px">Local (Large Truck)</span><span class="price">$115</span></div>
  </div>
  <div class="multi abs" style="left:477px;top:829px;width:210px">
    Local Deliveries 7 Mile Radius<br>
    <span class="item" style="display:flex">Excluding the Material</span>
    <span class="item" style="display:flex">Non Local</span>
  </div>
  <div class="quote">Call For<br>Quote</div>

  <div class="frame" style="left:838px;top:62px;width:321px;height:653px"></div>
  <div class="equip-head">
    <div class="top">EQUIPMENT WITH<br>OPERATOR AVAILABLE</div>
    <div class="bottom">CALL FOR PRICING</div>
  </div>
  <div class="rules" style="top:137px">
    <div class="r"><span>Onsite Mobile Grinding/Tub Grinding</span></div>
    <div class="r"><span>Forestry Mulching</span></div>
    <div class="r"><span>Skid Steer: (Rubber Track)</span></div>
    <div class="r"><span>Available Attachment</span></div>
    <div class="r"><span>Power Rake</span><span>3/4 Yard Bucket</span></div>
    <div class="r"><span>Forestry Mulching</span><span>Hydraulic Auger</span></div>
    <div class="r"><span></span><span>Grapple Bucket</span></div>
  </div>

  <div class="bar" style="top:295px">EXCAVATUR</div>
  <div class="rules" style="top:334px">
    <div class="r"><span>35 Class (7,500bs)</span></div>
    <div class="r"><span>60 Class (14,000bs)</span></div>
    <div class="r"><span>140 Class (45,500bs)</span></div>
    <div class="r"><span>160 Class (38,500bs)</span></div>
    <div class="r"><span>250 Class (60,000bs)</span></div>
  </div>

  <div class="bar" style="top:452px">BULL DOZER</div>
  <div class="rules" style="top:492px">
    <div class="r"><span>450 Class (18,000bs)</span></div>
    <div class="r"><span>700 Class (30,000bs)</span></div>
    <div class="r"><span>Vibratory Roller</span></div>
  </div>

  <div class="bar" style="top:571px">Rock Hammer</div>
  <div class="rules" style="top:610px">
    <div class="r"><span>Hydraulic Rock Hammer on 160 Class excavator.</span></div>
    <div class="r"><span>Additional mobilization fee for 1st day</span></div>
    <div class="r"><span>Tri-Axle Dump</span></div>
    <div class="r"><span>Dump Trailer</span></div>
  </div>

  <div class="know">
    <svg width="36" height="30" viewBox="0 0 36 30" aria-hidden="true">
      <path d="M4 12 L20 5 L20 23 L4 17 Z" fill="#fff"/>
      <rect x="6" y="17" width="4" height="9" fill="#fff"/>
      <path d="M24 8 L30 4 M25 14 L32 14 M24 20 L30 24" stroke="#fff" stroke-width="2" fill="none"/>
    </svg>
    DID YOU KNOW?
  </div>
  <p class="know-text">We Offer Onside Tub Grinding<br>&amp;<br><span class="accent">We are a GREEN RECYCLING Location!</span></p>

  <p class="footer">NON LOCAL CALL FOR PRICING. THANK YOU</p>
</main>
</body>
</html>
```